Photography business needs a money-off coupon design to be sent out by text

I'm a headshot photographer and I want to start a 'refer a friend' programme. Each time I take someone's headshot, I want to be able to give them a money-off coupon, featuring their own headshot, that they can send to their own network by text, offering a 20% discount to the recipient on a headshot session.

I need the design as a layered PSD file, so that I can drop in a different headshot for each client. Because the coupon will be being sent by text, I need it to be as simple and striking as possible. The design should meet the following criteria:

- It should feature my logo (two versions attached)

- It should feature one headshot - needs to be the main feature of the design. I have attached three examples from a typical session - as you will see, I use different backgrounds, so the design should be able to accommodate different colours.

- The following copy:

Milo Gives You 20% off (name will change with different headshots)

£30 off your next headshot session
Just text this referral card to make your appointment
Owen Hartley 07942 316 587
Normal Price £150, Now £130
www.framebrightly.co.uk

- The design should be portrait rather than landscape, given that that's how most people tend to use their phones vertically when they first look at a text message

- I need the designer to think about how the coupon will render on mobile phones; I think that it probably makes most sense to size the image in line with whichever smartphone has the highest resolution screen (probably vireo k4 or lumo 5), as that way the image will look good on all phone screens. Although I am happy to take the designer's advice on this and on optimum aspect ratio.

- Any other advice the designer can give me about the optimal design for text marketing of this nature will strongly impact on my final decision.

PLEASE NOTE: I've just uploaded a very basic layout that I did in Adobe Spark - I'm not expecting designers to follow it, but it does contain the key elements

Thanks,

Owen

Target Market(s)

Actors

Industry/Entity Type

Photographer

Font styles to use
Sans Serif

Colors

Designer to choose colors to be used in the design.

Requirements
Must have
• Clear communication of discount and redemption mechanism. Headshot image to be the most prominent feature. Must render clearly in different types of smartphone
Nice to have
• If possible, a link to my website (don't know if this is technically possible)
Should not have
• Colours which clash with my logo / the featured image

```html
<!DOCTYPE html>
<html lang="en">
<head>
<meta charset="utf-8">
<title>Headshot Referral Coupon</title>
<link rel="stylesheet" href="https://fonts.googleapis.com/css2?family=PT+Sans:wght@400&display=swap">
<style>
  :root {
    --page-bg: #ffffff;
    --sky: #dce8f3;
    --foliage: #7f9a5a;
    --skin: #b58c7a;
    --denim: #5a7fa8;
    --panel-dark: rgba(78, 78, 80, 0.68);
    --panel-mid: rgba(150, 150, 155, 0.55);
    --panel-low: rgba(55, 62, 80, 0.62);
    --bracket: #ffffff;
    --bracket-soft: rgba(255, 255, 255, 0.6);
    --text: #ffffff;
    --accent: #dff23c;
  }
  * { margin: 0; padding: 0; box-sizing: border-box; }
  html, body { width: 1200px; height: 1200px; overflow: hidden; background: var(--page-bg); }
  .coupon {
    position: relative;
    width: 1200px;
    height: 1200px;
    font-family: "PT Sans", sans-serif;
    color: var(--text);
  }
  .headshot {
    position: absolute;
    left: 158px; top: 40px;
    width: 884px; height: 1120px;
    background:
      radial-gradient(ellipse 34% 40% at 50% 42%, var(--skin) 0%, rgba(181,140,122,0.6) 55%, rgba(181,140,122,0) 100%),
      linear-gradient(90deg, rgba(127,154,90,0.85) 0%, rgba(127,154,90,0) 22%, rgba(127,154,90,0) 78%, rgba(127,154,90,0.85) 100%),
      linear-gradient(180deg, var(--sky) 0%, #c9d6d8 35%, #8f9a86 60%, var(--denim) 78%, #4d6f98 100%);
  }
  .panel { position: absolute; left: 284px; width: 634px; }
  .panel--offer { top: 160px; height: 510px; background: var(--panel-dark); }
  .panel--booking { top: 670px; height: 230px; background: var(--panel-mid); }
  .panel--web { top: 900px; height: 140px; background: var(--panel-low); }

  .frame-mark { position: absolute; left: 0; top: 0; }
  .text {
    position: absolute;
    left: 284px; width: 634px;
    text-align: center;
    line-height: 1;
    white-space: nowrap;
  }
  .headline { font-size: 66px; letter-spacing: 0.5px; }
  .headline--one { top: 236px; }
  .headline--two { top: 310px; }
  .saving { top: 398px; font-size: 30px; }
  .price-now { top: 486px; font-size: 52px; color: var(--accent); }
  .price-was { top: 555px; font-size: 55px; text-shadow: 2px 3px 4px rgba(0,0,0,0.55); }
  .booking { top: 689px; font-size: 40px; line-height: 50px; }
  .brand {
    top: 926px; font-size: 30px;
    display: flex; justify-content: center; align-items: center; gap: 12px;
  }
  .brand-square { width: 18px; height: 18px; background: var(--text); }
  .website { top: 984px; font-size: 24px; }
</style>
</head>
<body>
<main class="coupon">
  <div class="headshot" role="img" aria-label="Client headshot photograph, outdoors, wearing a denim jacket"></div>

  <div class="panel panel--offer"></div>
  <div class="panel panel--booking"></div>
  <div class="panel panel--web"></div>

  <svg class="frame-mark" width="1200" height="1200" viewBox="0 0 1200 1200" aria-hidden="true">
    <g fill="var(--bracket)">
      <rect x="244" y="122" width="18" height="144"/>
      <rect x="244" y="122" width="125" height="18"/>
      <rect x="939" y="936" width="18" height="144"/>
      <rect x="832" y="1062" width="125" height="18"/>
    </g>
    <g fill="none" stroke="var(--bracket-soft)" stroke-width="14">
      <rect x="867" y="134" width="80" height="93"/>
      <rect x="257" y="975" width="78" height="94"/>
    </g>
  </svg>

  <div class="text headline headline--one">MILO GIVES YOU</div>
  <div class="text headline headline--two">20% OFF</div>
  <div class="text saving">£30 off your next headshot session</div>
  <div class="text price-now">Now £130</div>
  <div class="text price-was">- normal price £150</div>
  <div class="text booking">Just text this referral card<br>to make your appointment<br>Owen Hartley<br>07942 316 587</div>
  <div class="text brand"><span class="brand-square"></span><span class="brand-name">Frame Brightly</span></div>
  <div class="text website">www.framebrightly.co.uk</div>
</main>
</body>
</html>
```